Business Cards for an 'affordable luxury' inner city home builder in Calgary.

We need a business card design that emulates the progressive, innovative, culture of our company and the modern style of our homes. Use our website www.velmarbuilds-ex.com as a reference for the product we build.

Our company builds homes in the inner city space of Calgary, Alberta. We build affordable luxury.

Target Market(s)

Young professional Families

Contact Information for Business Card

Try to maintain consistency with the logo font and the card font.

Requirements
Must have
• The details must include: Name, education, title, phone number, website and email (Address is not as important)
• The design must be uniques (like our logo), elegant, sophisticated and modern.

```html
<!DOCTYPE html>
<html lang="en">
<head>
<meta charset="utf-8">
<title>Velmar Builds Ltd — Business Card</title>
<link rel="stylesheet" href="https://fonts.googleapis.com/css2?family=Montserrat:wght@300;500;600&family=Roboto:wght@400&display=swap">
<style>
  :root {
    --backdrop: #2b2b2b;
    --backdrop-edge: #151515;
    --card-dark: #0d0d0d;
    --card-dark-sheen: #1e1e1e;
    --card-light: #f4f4f4;
    --card-light-shade: #dedede;
    --ink: #1c1c1c;
    --ink-soft: #555555;
    --icon: #6e6e6e;
    --paper-text: #ffffff;
    --rule: #3a3a3a;
  }
  * { margin: 0; padding: 0; box-sizing: border-box; }
  html, body { width: 1200px; height: 1200px; overflow: hidden; }
  body {
    background: radial-gradient(ellipse at 50% 35%, var(--backdrop), var(--backdrop-edge));
    position: relative;
    font-family: "Roboto", Arial, sans-serif;
  }
  .card {
    position: absolute;
    left: 250px;
    width: 700px;
    height: 400px;
    border-radius: 28px;
    overflow: hidden;
    box-shadow: 0 18px 40px rgba(0,0,0,.55);
  }
  /* Front */
  .card-front {
    top: 170px;
    background: linear-gradient(135deg, var(--card-dark-sheen), var(--card-dark) 55%);
  }
  .front-mark {
    position: absolute;
    left: 60px; top: 70px;
    width: 230px; height: 230px;
    background: rgba(255,255,255,.05);
  }
  .front-name {
    position: absolute;
    left: 375px; top: 130px;
    font-family: "Montserrat", sans-serif;
    font-weight: 500;
    font-size: 38px;
    line-height: 1.05;
    letter-spacing: 2px;
    color: var(--paper-text);
    text-transform: uppercase;
  }
  /* Back */
  .card-back {
    top: 630px;
    background: var(--card-light);
  }
  .facet-field {
    position: absolute; inset: 0;
    background:
      linear-gradient(120deg, transparent 35%, rgba(255,255,255,.8) 50%, transparent 65%),
      linear-gradient(200deg, var(--card-light) 20%, var(--card-light-shade) 60%, var(--card-light) 90%);
  }
  .brand {
    position: absolute;
    left: 48px; top: 42px;
    display: flex; align-items: center; gap: 18px;
  }
  .brand-square { width: 70px; height: 70px; background: var(--ink); }
  .brand-letters {
    font-family: "Montserrat", sans-serif;
    font-weight: 500;
    font-size: 24px;
    line-height: 1.15;
    color: var(--ink);
    display: flex; flex-direction: column; align-items: center;
  }
  .person {
    position: absolute;
    right: 45px; top: 120px;
    text-align: right;
    color: var(--ink);
  }
  .person-name {
    font-family: "Montserrat", sans-serif;
    font-size: 38px;
    line-height: 1.1;
  }
  .person-name .first { font-weight: 300; }
  .person-name .last { font-weight: 600; }
  .person-role { font-size: 19px; line-height: 1.3; margin-top: 2px; }
  .rule {
    position: absolute; top: 250px; height: 2px; background: var(--rule);
  }
  .rule-left { left: 45px; width: 320px; }
  .rule-right { left: 380px; width: 275px; background: var(--ink-soft); }
  .contact-list {
    position: absolute; left: 45px; top: 272px;
    list-style: none;
  }
  .contact-list li, .location-list li {
    display: flex; align-items: center; gap: 14px;
    font-size: 20px; color: var(--ink);
    height: 34px;
  }
  .location-list {
    position: absolute; right: 45px; top: 282px;
    list-style: none;
  }
  .location-list li { justify-content: flex-end; }
  .icon { width: 22px; height: 22px; flex: none; fill: var(--icon); }
  .social-dot {
    width: 20px; height: 20px; border-radius: 50%;
    border: 2px solid var(--icon); flex: none;
  }
</style>
</head>
<body>

<section class="card card-front">
  <div class="front-mark" aria-hidden="true"></div>
  <h1 class="front-name">Velmar<br>Builds Ltd</h1>
</section>

<section class="card card-back">
  <div class="facet-field" role="img" aria-label="Faceted light-grey geometric background"></div>

  <div class="brand">
    <div class="brand-square" aria-hidden="true"></div>
    <div class="brand-letters"><span>V</span><span>B</span></div>
  </div>

  <div class="person">
    <div class="person-name"><span class="first">Aaron</span> <span class="last">Lindqvist</span></div>
    <div class="person-role">Managing Director / Contractor</div>
    <div class="person-role">Education Details</div>
  </div>

  <div class="rule rule-left"></div>
  <div class="rule rule-right"></div>

  <ul class="contact-list">
    <li>
      <svg class="icon" viewBox="0 0 24 24"><path d="M6.6 10.8a15 15 0 0 0 6.6 6.6l2.2-2.2a1 1 0 0 1 1-.25 11.4 11.4 0 0 0 3.6.57 1 1 0 0 1 1 1V20a1 1 0 0 1-1 1A17 17 0 0 1 3 4a1 1 0 0 1 1-1h3.5a1 1 0 0 1 1 1c0 1.25.2 2.45.57 3.6a1 1 0 0 1-.25 1z"/></svg>
      403-555-0184
    </li>
    <li>
      <svg class="icon" viewBox="0 0 24 24"><path d="M2 5h20v14H2z M2 5l10 8 10-8" fill="none" stroke="#6e6e6e" stroke-width="2"/></svg>
      projects@velmarbuilds-ex.com
    </li>
    <li>
      <svg class="icon" viewBox="0 0 24 24" fill="none" stroke="#6e6e6e" stroke-width="1.8"><circle cx="12" cy="12" r="9.5"/><ellipse cx="12" cy="12" rx="4" ry="9.5"/><path d="M2.5 12h19M4 7h16M4 17h16"/></svg>
      www.velmarbuilds-ex.com
    </li>
  </ul>

  <ul class="location-list">
    <li>
      482 14 Ave NW, Calgary, AB
      <svg class="icon" viewBox="0 0 24 24"><path d="M12 2a7 7 0 0 0-7 7c0 5 7 13 7 13s7-8 7-13a7 7 0 0 0-7-7zm0 9.5A2.5 2.5 0 1 1 12 6.5a2.5 2.5 0 0 1 0 5z"/></svg>
    </li>
    <li>
      Velmarbuilds
      <span class="social-dot" aria-hidden="true"></span>
    </li>
  </ul>
</section>

</body>
</html>
```